Venture Capital Investment Firm

We are looking to overhaul our existing website (substantially), with only using the same logos (which we can provide).
We are an investment firm that focuses on making loans to late stage technology companies. Our site should ultimately look like other venture capital firms, and look modern and fresh. We have an existing website www.merrowfinch.com which this will be replacing, although we will be using a lot of the existing written content, and potentially the numbers of pages we will need, we are not wed to anything else. Please feel free to shoot any questions at any time and thank you in advance for your help!
Websites we like as examples:
https://www.tovalynbrook.com/
https://www.quenridgefund.com/
Target Market(s)
Potential investors who will invest in our firm, as well as potentially companies that are looking to borrow money from us.
Coding
Number of Pages Required
5+ page
Colors
Designer to choose colors to be used in the design.
Look and feel

```html
<!DOCTYPE html>
<html lang="en">
<head>
<meta charset="utf-8">
<title>Merrow Finch — Structured Credit Investment</title>
<link href="https://fonts.googleapis.com/css2?family=Crimson+Pro:wght@400;500&family=Mulish:wght@300;400;600&display=swap" rel="stylesheet">
<style>
  :root {
    --navy-deep: #03022f;
    --navy-hero: #2b2867;
    --navy-band: #14124a;
    --navy-footer: #0a0933;
    --accent: #f0a32d;
    --white: #ffffff;
    --ink: #1d1c3a;
    --rule: #1f1c5c;
  }
  * { margin: 0; padding: 0; box-sizing: border-box; }
  html, body { width: 1200px; height: 3356px; overflow: hidden; }
  body { position: relative; background: var(--white); font-family: "Mulish", sans-serif; color: var(--ink); }
  .serif { font-family: "Crimson Pro", serif; }

  /* Hero */
  .hero {
    position: absolute; left: 0; top: 0; width: 1200px; height: 748px;
    background: linear-gradient(180deg, #2c2a6b 0%, #36336f 35%, #2a2763 70%, #221f58 100%);
  }
  .brand { position: absolute; display: flex; align-items: center; gap: 10px; color: var(--white); font-family: "Crimson Pro", serif; font-size: 30px; font-weight: 400; letter-spacing: 0.5px; }
  .brand-mark { width: 14px; height: 14px; border-radius: 50%; background: var(--white); }
  .hero .brand { left: 120px; top: 24px; }
  .nav { position: absolute; right: 120px; top: 38px; display: flex; gap: 22px; list-style: none; }
  .nav li { color: var(--white); font-size: 11px; font-weight: 600; letter-spacing: 0.3px; }
  .hero-title {
    position: absolute; left: 0; width: 1200px; top: 308px; text-align: center;
    color: var(--white); font-size: 33px; line-height: 38.5px; font-weight: 400; letter-spacing: 0.3px;
  }
  .btn {
    position: absolute; display: flex; align-items: center; justify-content: center;
    background: var(--accent); color: var(--white); font-family: "Crimson Pro", serif;
    font-size: 15px; letter-spacing: 0.8px; width: 209px; height: 45px;
  }
  .hero .btn { left: 495px; top: 456px; }

  /* Intro */
  .intro-title { position: absolute; left: 0; width: 1200px; top: 852px; text-align: center; font-size: 25px; font-weight: 500; color: #0d0c2e; letter-spacing: 0.3px; }
  .intro-rule { position: absolute; left: 549px; top: 898px; width: 102px; height: 2px; background: var(--rule); }
  .intro-text { position: absolute; left: 203px; width: 800px; top: 936px; text-align: center; font-size: 18.5px; line-height: 26.5px; font-weight: 400; color: #1d1c2f; }

  /* Feature blocks */
  .photo { position: absolute; width: 568px; height: 520px; }
  .panel { position: absolute; width: 517px; height: 375px; background: var(--navy-deep); color: var(--white); padding: 46px 53px 0; }
  .panel h2 { font-family: "Crimson Pro", serif; font-weight: 500; font-size: 26px; letter-spacing: 0.3px; margin-bottom: 18px; }
  .panel ul { list-style: none; font-size: 14.5px; line-height: 24px; font-weight: 300; margin-bottom: 14px; }
  .panel ul li::before { content: "• "; }
  .panel .lead { font-size: 14.5px; line-height: 24px; font-weight: 300; margin-bottom: 14px; }
  .panel p { font-size: 13.5px; line-height: 20px; font-weight: 300; }
  .panel .btn { position: absolute; left: 53px; bottom: 55px; }

  .photo-experience { left: 512px; top: 1182px; background: linear-gradient(135deg, #3a3a3a, #8a8a8a 50%, #2c2c2c); }
  .panel-experience { left: 120px; top: 1255px; }
  .photo-industry { left: 120px; top: 1793px; background: linear-gradient(160deg, #d4d4d4, #6c6c6c 50%, #2e2e2e); }
  .panel-industry { left: 563px; top: 1865px; }
  .photo-benefits { left: 512px; top: 2405px; background: linear-gradient(135deg, #9a9a9a, #dadada 45%, #5e5e5e); }
  .panel-benefits { left: 120px; top: 2477px; }

  /* Newsletter */
  .newsletter { position: absolute; left: 0; top: 3014px; width: 1200px; height: 138px; background: var(--navy-band); color: var(--white); }
  .newsletter-label { position: absolute; right: 810px; top: 52px; text-align: right; }
  .newsletter-label h3 { font-family: "Crimson Pro", serif; font-weight: 500; font-size: 16px; letter-spacing: 0.3px; line-height: 18px; }
  .newsletter-label span { font-size: 12px; font-weight: 300; }
  .newsletter-input { position: absolute; left: 410px; top: 49px; width: 459px; height: 40px; background: var(--white); color: #555; font-size: 15px; padding: 11px 20px; }
  .newsletter-join { position: absolute; left: 869px; top: 49px; width: 133px; height: 40px; border: 1px solid #b7b6d6; display: flex; align-items: center; justify-content: center; font-size: 15px; font-weight: 300; }

  /* Footer */
  .footer { position: absolute; left: 0; top: 3152px; width: 1200px; height: 204px; background: var(--navy-footer); color: var(--white); }
  .footer .brand { left: 120px; top: 73px; }
  .copyright { position: absolute; left: 120px; top: 126px; font-size: 11.5px; font-weight: 300; }
  .footer-col { position: absolute; top: 66px; font-size: 11.5px; line-height: 18px; font-weight: 300; }
  .footer-col h4 { font-size: 11.5px; font-weight: 400; margin-bottom: 10px; }
  .footer-address { left: 559px; }
  .footer-contact { left: 898px; }
</style>
</head>
<body>

<header class="hero" role="img" aria-label="City skyline at dusk with a tall spire, tinted deep navy">
  <div class="brand"><span class="brand-mark"></span>Merrow Finch</div>
  <ul class="nav">
    <li>HOME</li><li>STRATEGY</li><li>ABOUT US</li><li>TEAM</li><li>NEWS</li><li>CONTACT</li><li>INVESTOR</li>
  </ul>
  <h1 class="hero-title serif">WE ARE A GLOBAL STRUCTURED CREDIT<br>INVESTMENT FIRM FOCUSED ON THE<br>HEALTHCARE AND TECHNOLOGY INDUSTRIES</h1>
  <div class="btn">OUR STRATEGY</div>
</header>

<section class="intro">
  <h2 class="intro-title serif">MERROW FINCH STARTED WITH A BIG IDEA</h2>
  <div class="intro-rule"></div>
  <p class="intro-text">Merrow Finch is a private investment firm unique in its dual focus on life science and technology credit opportunities.&nbsp; Our ambidextrous approach to investing reflects a broad recognition and appreciation for the critical role intellectual property plays in the successful commercialization of products.&nbsp; We apply our extensive industry expertise to assess the revenue visibility created by these assets and offer a range of creative financing solutions.</p>
</section>

<div class="photo photo-experience" role="img" aria-label="Black and white photo of a smiling professional working at a laptop"></div>
<section class="panel panel-experience">
  <h2>OUR EXPERIENCE</h2>
  <ul>
    <li>OVER $1.2B INVESTED BY OUR PARTNERS</li>
    <li>40+ LIFE SCIENCE AND TECHNOLOGY INVESTMENTS</li>
    <li>OVER A DECADE INNOVATING FINANCING STRUCTURES</li>
  </ul>
  <p>We bring over 40 years of collective experience to our invest-<br>ments, including over $1.2B invested within structured credit,<br>milestones and royalties.</p>
  <div class="btn">LEARN MORE</div>
</section>

<div class="photo photo-industry" role="img" aria-label="Black and white upward view of a tall skyscraper facade"></div>
<section class="panel panel-industry">
  <h2>INDUSTRY FOCUS</h2>
  <div class="lead">WE PROVIDE FLEXIBLE CAPITAL TO INNOVATIVE COMPA-<br>NIES AND THEIR INVESTORS</div>
  <p>Our focus spans the life science and technology industries,<br>two sectors where intellectual property (IP) is an integral<br>driver of asset and enterprise value.</p>
  <div class="btn">LEARN MORE</div>
</section>

<div class="photo photo-benefits" role="img" aria-label="Black and white close-up of a pile of silver dollar coins"></div>
<section class="panel panel-benefits">
  <h2>KEY BENEFITS</h2>
  <ul>
    <li>STRUCTURED CREDIT</li>
    <li>MILESTONES &amp; ROYALTIES</li>
    <li>LEGACY ASSETS</li>
  </ul>
  <p>We seek to fill a void in the capital markets where too often<br>complexity and perceived risk penalize innovative companies<br>with proven products.</p>
  <div class="btn">LEARN MORE</div>
</section>

<section class="newsletter">
  <div class="newsletter-label">
    <h3>JOIN OUR NEWSLETTER</h3>
    <span>Receive updates and special offers</span>
  </div>
  <div class="newsletter-input">Email</div>
  <div class="newsletter-join">JOIN</div>
</section>

<footer class="footer">
  <div class="brand"><span class="brand-mark"></span>Merrow Finch</div>
  <div class="copyright">© Copyright 2020</div>
  <div class="footer-col footer-address">
    <h4>MERROW FINCH, SAN FRANCISCO</h4>
    Building number #<br>Street Name, 01234, Earmark<br>Address, ZIP CODE
  </div>
  <div class="footer-col footer-contact">
    <h4>CONTACT</h4>
    Phone 123 456 789<br>Fax 123 456 789<br>Email emailaddress@email.com
  </div>
</footer>

</body>
</html>
```